BriarLoom Website Homepage Design

Please provide your idea of homepage for a hosting company. This project is for DESIGN only, no coding.

It must use/combine colors used in logo, clean, modern look.

Homepage must consist of at least 4 sections (example: testimonials, services, and so on. not necesarily all of them). We would like the navigation to be horizontal, but not mandatory.

You can include a preview of services page (optional, not a must).

Number of Pages Required

1 page

Font styles to use
Sans Serif

```html
<!DOCTYPE html>
<html lang="en">
<head>
<meta charset="utf-8">
<title>BriarLoom — Hosting Homepage</title>
<link href="https://fonts.googleapis.com/css2?family=Poppins:ital,wght@0,300;0,400;0,500;0,600;0,700;0,800;1,400&display=swap" rel="stylesheet">
<style>
:root{
  --blue:#0b86d9;
  --blue-2:#3a68e0;
  --blue-soft:#e8f2fc;
  --ink:#4a4a4a;
  --ink-dark:#333;
  --muted:#777;
  --line:#e6e6e6;
  --pill:#ececec;
  --footer:#525252;
  --footer-bar:#3e3e3e;
  --white:#fff;
}
*{box-sizing:border-box;margin:0;padding:0}
html,body{width:1200px;height:3844px;overflow:hidden}
body{position:relative;font-family:'Poppins',sans-serif;color:var(--ink);background:var(--white)}
.abs{position:absolute}
/* header */
.site-header{left:0;top:0;width:1200px;height:95px;background:var(--white)}
.brand{left:88px;top:28px;font-size:36px;font-weight:600;letter-spacing:1px;color:var(--blue);line-height:46px}
.brand .dot{display:inline-block;width:10px;height:10px;background:var(--blue);border-radius:50%;margin-left:6px;vertical-align:middle}
.main-nav{left:453px;top:40px;display:flex;gap:24px;font-size:13px;font-weight:500;color:#555;letter-spacing:.3px}
.btn-pill{display:flex;align-items:center;justify-content:center;border-radius:20px;font-size:13px;font-weight:600;letter-spacing:.3px}
.btn-signin{left:915px;top:32px;width:92px;height:37px;background:var(--pill);color:#555}
.btn-signup{left:1016px;top:32px;width:94px;height:37px;background:var(--blue);color:var(--white)}
/* hero */
.hero{left:0;top:95px;width:1200px;height:642px;background:linear-gradient(100deg,#0a87d9 0%,#1c7ddc 55%,#3b67e0 100%)}
.hero-eyebrow{left:89px;top:240px;font-size:30px;font-weight:300;color:var(--white);display:flex;align-items:center;gap:10px}
.hero-eyebrow::after{content:"";width:66px;height:2px;background:var(--white)}
.hero-title{left:87px;top:285px;font-size:61px;font-weight:800;line-height:54px;color:var(--white);letter-spacing:.5px}
.hero-sub{left:88px;top:412px;width:440px;font-size:15px;line-height:22px;color:var(--white)}
.btn-hero{left:88px;top:476px;width:139px;height:39px;background:rgba(255,255,255,.25);color:var(--white);font-size:13px;font-weight:600}
.hero-art{left:612px;top:127px;width:588px;height:455px;border-radius:40px;background:radial-gradient(ellipse at 55% 50%,rgba(255,255,255,.22),rgba(30,60,200,.18) 60%,rgba(255,255,255,0) 75%)}
/* domain */
.domain-box{left:173px;top:649px;width:854px;height:176px;background:var(--white);box-shadow:0 18px 40px rgba(0,0,0,.08)}
.domain-search{left:181px;top:42px;width:489px;height:51px;background:#ededed;border-radius:26px}
.domain-search span{position:absolute;left:26px;top:15px;font-size:16px;color:#999}
.domain-search b{position:absolute;right:5px;top:5px;width:108px;height:41px;border-radius:21px;background:var(--white);font-size:12px;font-weight:600;color:#444;display:flex;align-items:center;justify-content:center;letter-spacing:.4px}
.tlds{left:0;top:117px;width:854px;display:flex;justify-content:center;align-items:center}
.tld{display:flex;align-items:baseline;gap:12px;padding:0 30px;border-left:1px solid #ddd;line-height:22px}
.tld:first-child{border-left:none}
.tld strong{font-size:19px;font-weight:600}
.tld small{font-size:12px;color:#555}
/* section heads */
.eyebrow{left:0;width:1200px;text-align:center;font-size:14px;color:#555;letter-spacing:.3px}
.section-title{left:0;width:1200px;text-align:center;font-size:37px;font-weight:700;color:var(--ink);letter-spacing:.5px}
/* services */
.service-hub{left:474px;top:1007px;width:246px;height:246px;border-radius:50%;background:var(--blue)}
.service{width:320px}
.service h3{font-size:14.5px;font-weight:600;color:#444;letter-spacing:.4px;margin-bottom:6px}
.service p{font-size:13px;line-height:20px;color:#666}
.service.left{text-align:right}
.svc-icon{width:58px;height:58px}
.divider{left:90px;width:1020px;height:1px;background:var(--line)}
/* about */
.about-art{left:134px;top:1418px;width:441px;height:507px;border-radius:200px 200px 60px 60px;background:linear-gradient(180deg,#f1f2f4 0%,#cfe4fb 50%,#6fb0f2 100%)}
.about-eyebrow{left:644px;top:1524px;font-size:14px;color:#555}
.about-title{left:643px;top:1548px;font-size:37px;font-weight:700;line-height:36px;color:var(--ink)}
.about-text{left:644px;top:1638px;width:430px;font-size:14.5px;line-height:24px;color:#666}
.btn-dark{left:645px;top:1779px;width:121px;height:36px;background:#555;color:var(--white);font-size:13px}
/* cta */
.cta{left:0;top:2001px;width:1200px;height:330px;background:linear-gradient(100deg,#0a87d9 0%,#2a73de 60%,#3b67e0 100%)}
.cta-eyebrow{left:0;top:87px;width:1200px;text-align:center;font-size:15px;color:var(--white)}
.cta-title{left:0;top:104px;width:1200px;text-align:center;font-size:37px;font-weight:700;line-height:40px;color:var(--white);letter-spacing:.5px}
.btn-white{left:509px;top:203px;width:181px;height:44px;background:var(--white);color:#333;font-size:13px;box-shadow:0 8px 20px rgba(0,0,0,.12)}
.cloud{border-radius:40px;background:rgba(255,255,255,.22)}
/* testimonials */
.avatar{width:126px;height:126px;border-radius:50%;background:linear-gradient(180deg,#f3f3f3,#d6dde4);border:6px solid var(--white);box-shadow:0 10px 24px rgba(0,0,0,.12)}
.quote{width:320px;font-size:17.5px;font-style:italic;line-height:25px;color:#666}
.client{font-size:17px;font-weight:500;color:#444;letter-spacing:.5px}
/* blog */
.card{top:2949px;width:281px;height:399px;background:var(--white);box-shadow:0 14px 34px rgba(0,0,0,.08)}
.card-photo{width:281px;height:217px;background:linear-gradient(180deg,#c9c9c9,#a9a9a9)}
.card-meta{position:absolute;left:27px;top:258px;font-size:12px;color:#555}
.card-title{position:absolute;left:27px;top:285px;width:230px;font-size:14.5px;font-weight:600;line-height:19px;color:#444;letter-spacing:.4px}
.card-text{position:absolute;left:27px;top:334px;width:235px;font-size:12.5px;line-height:19px;color:#666}
/* footer */
.site-footer{left:0;top:3442px;width:1200px;height:342px;background:var(--footer)}
.footer-bar{left:0;top:3784px;width:1200px;height:60px;background:var(--footer-bar);color:var(--white);font-size:12px;font-weight:600;text-align:center;line-height:60px;letter-spacing:.3px}
.footer-brand{left:88px;top:3565px;font-size:40px;font-weight:500;color:var(--white);letter-spacing:1px;line-height:46px}
.social{top:3625px;width:30px;height:30px;border-radius:50%;background:#666;color:var(--white);font-size:12px;display:flex;align-items:center;justify-content:center}
.footer-head{font-size:14px;font-weight:600;color:var(--white);letter-spacing:.5px}
.footer-links{list-style:none;font-size:12.5px;color:var(--white);line-height:31px}
.contact-row{display:flex;gap:8px;font-size:13px;line-height:21px;color:var(--white)}
.contact-row svg{flex:none;margin-top:4px}
.news-text{left:852px;top:3560px;width:230px;font-size:12.5px;line-height:19px;color:var(--white)}
.news-input{left:852px;top:3610px;width:218px;height:43px;background:var(--white);font-size:12.5px;color:#555;display:flex;align-items:center;padding-left:18px;gap:8px}
.news-btn{left:1070px;top:3610px;width:40px;height:43px;background:var(--blue);display:flex;align-items:center;justify-content:center}
.to-top{left:1137px;top:3751px;width:36px;height:36px;border-radius:50%;background:var(--white);display:flex;align-items:center;justify-content:center}
</style>
</head>
<body>

<header class="abs site-header">
  <div class="abs brand">BriarLoom<span class="dot"></span></div>
  <nav class="abs main-nav"><span>HOME</span><span>ABOUT</span><span>SERVICE</span><span>HOSTING</span><span>NEWS</span><span>CONTACT</span></nav>
  <div class="abs btn-pill btn-signin">SIGN IN</div>
  <div class="abs btn-pill btn-signup">SIGN UP</div>
</header>

<section class="abs hero">
  <div class="abs hero-art" role="img" aria-label="Isometric illustration of server towers on a glowing network grid"></div>
</section>
<div class="abs hero-eyebrow">WE PROVIDE</div>
<h1 class="abs hero-title">BEST HOSTING<br>SOLUTIONS...</h1>
<p class="abs hero-sub">Share processes an data secure lona need to know basis without the need...</p>
<div class="abs btn-pill btn-hero">GET STARTED</div>

<div class="abs domain-box">
  <div class="abs domain-search"><span>domain.com</span><b>SEARCH</b></div>
  <div class="abs tlds">
    <div class="tld"><strong style="color:#0b86d9">.com</strong><small>$9.95</small></div>
    <div class="tld"><strong style="color:#5b2a86">.co</strong><small>$7.95</small></div>
    <div class="tld"><strong style="color:#f07c1c">.info</strong><small>$2.95</small></div>
    <div class="tld"><strong style="color:#222">.net</strong><small>$5.95</small></div>
    <div class="tld"><strong style="color:#777">.store</strong><small>$2.95</small></div>
  </div>
</div>

<div class="abs eyebrow" style="top:920px">FEATURES</div>
<h2 class="abs section-title" style="top:938px">OUR BEST SERVICE</h2>

<div class="abs service-hub">
  <svg width="246" height="246" viewBox="0 0 246 246" aria-hidden="true">
    <g fill="#fff">
      <rect x="56" y="66" width="134" height="32" rx="6"/>
      <rect x="56" y="107" width="134" height="32" rx="6"/>
      <rect x="56" y="148" width="134" height="32" rx="6"/>
    </g>
    <g fill="#0b86d9">
      <rect x="70" y="75" width="3" height="14"/><rect x="77" y="75" width="3" height="14"/><rect x="84" y="75" width="3" height="14"/><circle cx="176" cy="82" r="5"/>
      <rect x="70" y="116" width="3" height="14"/><rect x="77" y="116" width="3" height="14"/><rect x="84" y="116" width="3" height="14"/><circle cx="176" cy="123" r="5"/>
      <rect x="70" y="157" width="3" height="14"/><rect x="77" y="157" width="3" height="14"/><rect x="84" y="157" width="3" height="14"/><circle cx="176" cy="164" r="5"/>
    </g>
  </svg>
</div>

<div class="abs service left" style="left:47px;top:1025px"><h3>SHARED HOSTING</h3><p>Aenean sollicitudin lorem quis nisi<br>elit consequat ipsum...</p></div>
<svg class="abs svc-icon" style="left:384px;top:1025px" viewBox="0 0 58 58" fill="none" stroke="#0b86d9" stroke-width="2" aria-hidden="true">
  <path d="M14 24a8 8 0 0 1 4-14 12 12 0 0 1 22 2 7 7 0 0 1 2 12z"/><line x1="29" y1="24" x2="29" y2="34"/><path d="M12 34h34"/>
  <ellipse cx="12" cy="42" rx="6" ry="3"/><path d="M6 42v8c0 2 12 2 12 0v-8"/><ellipse cx="29" cy="42" rx="6" ry="3"/><path d="M23 42v8c0 2 12 2 12 0v-8"/><ellipse cx="46" cy="42" rx="6" ry="3"/><path d="M40 42v8c0 2 12 2 12 0v-8"/>
</svg>

<div class="abs service left" style="left:47px;top:1149px"><h3>RESELLER HOSTING</h3><p>Aenean sollicitudin lorem quis nisi<br>elit consequat ipsum...</p></div>
<svg class="abs svc-icon" style="left:384px;top:1150px" viewBox="0 0 58 58" fill="none" stroke="#0b86d9" stroke-width="2" aria-hidden="true">
  <circle cx="22" cy="24" r="18"/><ellipse cx="22" cy="24" rx="8" ry="18"/><line x1="4" y1="24" x2="40" y2="24"/><line x1="7" y1="15" x2="37" y2="15"/><line x1="7" y1="33" x2="37" y2="33"/>
  <rect x="30" y="32" width="24" height="8" fill="#fff"/><rect x="30" y="41" width="24" height="8" fill="#fff"/><rect x="30" y="50" width="24" height="7" fill="#fff"/>
</svg>

<div class="abs service" style="left:833px;top:1025px"><h3>CLOUD HOSTING</h3><p>Aenean sollicitudin lorem quis nisi<br>elit consequat ipsum...</p></div>
<svg class="abs svc-icon" style="left:754px;top:1027px" viewBox="0 0 58 58" fill="none" stroke="#0b86d9" stroke-width="2" aria-hidden="true">
  <circle cx="14" cy="14" r="7"/><circle cx="14" cy="14" r="2.5"/><path d="M26 28a8 8 0 0 1 6-12 10 10 0 0 1 18 4 6 6 0 0 1 0 10z"/>
  <rect x="6" y="30" width="26" height="18" rx="2"/><line x1="19" y1="48" x2="19" y2="54"/><line x1="12" y1="54" x2="26" y2="54"/><line x1="36" y1="38" x2="52" y2="38"/><line x1="36" y1="45" x2="48" y2="45"/>
</svg>

<div class="abs service" style="left:833px;top:1149px"><h3>DEDICATED HOSTING</h3><p>Aenean sollicitudin lorem quis nisi<br>elit consequat ipsum...</p></div>
<svg class="abs svc-icon" style="left:754px;top:1150px" viewBox="0 0 58 58" fill="none" stroke="#0b86d9" stroke-width="2" aria-hidden="true">
  <rect x="3" y="4" width="32" height="12" rx="2"/><rect x="3" y="20" width="32" height="12" rx="2"/><rect x="3" y="36" width="32" height="12" rx="2"/>
  <rect x="24" y="14" width="30" height="40" rx="2" fill="#fff"/><line x1="29" y1="22" x2="49" y2="22"/><line x1="29" y1="30" x2="49" y2="30"/><line x1="29" y1="38" x2="49" y2="38"/><line x1="29" y1="46" x2="44" y2="46"/>
</svg>

<div class="abs divider" style="top:1343px"></div>

<div class="abs about-art" role="img" aria-label="Isometric illustration of a server cluster in front of a soft cloud"></div>
<div class="abs about-eyebrow">ABOUT US</div>
<h2 class="abs about-title">GET BEST PLANS FOR<br>MORE POWER</h2>
<p class="abs about-text">Etiam rhoncus maecenas tempus, tellus eget condim entum rhon cus sem quam semper libero sit amet adipisc ing sem neque sed ipsum nam quam&nbsp; Rhoncus maecenas tempus, tellus eget condim entum rhon cus sem quam semper libero sit amet.</p>
<div class="abs btn-pill btn-dark">READ MORE</div>

<section class="abs cta">
  <div class="abs cloud" style="left:110px;top:130px;width:128px;height:72px" role="img" aria-label="Cloud shape"></div>
  <div class="abs cloud" style="left:950px;top:130px;width:128px;height:72px" role="img" aria-label="Cloud shape"></div>
  <div class="abs cloud" style="left:788px;top:214px;width:70px;height:36px" role="img" aria-label="Small cloud shape"></div>
  <div class="abs cta-eyebrow">2500+ PEOPLE TRUSTED ON BRIARLOOM</div>
  <h2 class="abs cta-title">READY TO WORK WITH BRIARLOOM?<br>REGISTER TODAY</h2>
  <div class="abs btn-pill btn-white">GET STARTED NOW</div>
</section>

<div class="abs eyebrow" style="top:2414px">TESTIMONIALS</div>
<h2 class="abs section-title" style="top:2434px">WHAT OUR CLIENT SAY</h2>

<div class="abs avatar" style="left:94px;top:2583px" role="img" aria-label="Portrait of client Sara Doe"></div>
<p class="abs quote" style="left:242px;top:2576px">Aenean sollicitudinlorem qui auctor nisi elit consequat ipsum, nec sagittis sem nibh id elit. Duis sed odio sit amet nibh vulputate cursus a sit</p>
<div class="abs client" style="left:241px;top:2692px">SARA DOE</div>

<div class="abs avatar" style="left:644px;top:2583px" role="img" aria-label="Portrait of client John Doe"></div>
<p class="abs quote" style="left:794px;top:2576px">Aenean sollicitudinlorem qui auctor nisi elit consequat ipsum, nec sagittis sem nibh id elit. Duis sed odio sit amet nibh vulputate cursus a sit</p>
<div class="abs client" style="left:792px;top:2692px">JOHN DOE</div>

<div class="abs divider" style="top:2793px"></div>

<div class="abs eyebrow" style="top:2866px">BLOG</div>
<h2 class="abs section-title" style="top:2886px">GET LATEST INFO</h2>

<article class="abs card" style="left:162px">
  <div class="card-photo" role="img" aria-label="Photo of a smiling man holding a laptop"></div>
  <div class="card-meta">byJohn &nbsp;•&nbsp; January 2021</div>
  <h3 class="card-title">STAY UP-TO-DATE WITH OUR LATEST NEWS.</h3>
  <p class="card-text">Aenean sollicitudin lorem bibendum auctor, nisi elit consequat...</p>
</article>
<article class="abs card" style="left:459px">
  <div class="card-photo" role="img" aria-label="Photo of a man in a suit holding a laptop"></div>
  <div class="card-meta">byJohn &nbsp;•&nbsp; January 2021</div>
  <h3 class="card-title">STAY UP-TO-DATE WITH OUR LATEST NEWS.</h3>
  <p class="card-text">Aenean sollicitudin lorem bibendum auctor, nisi elit consequat...</p>
</article>
<article class="abs card" style="left:757px">
  <div class="card-photo" role="img" aria-label="Photo of a man in a light shirt using a laptop"></div>
  <div class="card-meta">byJohn &nbsp;•&nbsp; January 2021</div>
  <h3 class="card-title">STAY UP-TO-DATE WITH OUR LATEST NEWS.</h3>
  <p class="card-text">Aenean sollicitudin lorem bibendum auctor, nisi elit consequat...</p>
</article>

<footer class="abs site-footer"></footer>
<div class="abs footer-brand">BriarLoom</div>
<div class="abs social" style="left:145px">f</div>
<div class="abs social" style="left:184px">t</div>
<div class="abs social" style="left:224px">in</div>
<div class="abs social" style="left:263px">g</div>

<div class="abs footer-head" style="left:421px;top:3512px">QUICK LINKS</div>
<ul class="abs footer-links" style="left:421px;top:3552px">
  <li>About Us</li><li>Product &amp; Services</li><li>Solutions</li><li>Blog</li><li>Contact Us</li>
</ul>

<div class="abs footer-head" style="left:604px;top:3512px">CONTACT INFO</div>
<div class="abs contact-row" style="left:604px;top:3556px">
  <svg width="14" height="10" viewBox="0 0 14 10" aria-hidden="true"><rect width="14" height="10" rx="1" fill="#1a9ae8"/><path d="M0 1l7 5 7-5" stroke="#fff" fill="none"/></svg>
  <div>Email:<br>hello@briarloom.net</div>
</div>
<div class="abs contact-row" style="left:604px;top:3618px">
  <svg width="14" height="14" viewBox="0 0 14 14" aria-hidden="true"><path d="M3 1l3 3-2 2a8 8 0 0 0 4 4l2-2 3 3-2 2C6 13 1 8 1 3z" fill="#1a9ae8"/></svg>
  <div>Phone:<br>(855) 550-1842</div>
</div>
<div class="abs contact-row" style="left:604px;top:3679px">
  <svg width="14" height="16" viewBox="0 0 14 16" aria-hidden="true"><path d="M7 16S1 9 1 6a6 6 0 0 1 12 0c0 3-6 10-6 10z" fill="#1a9ae8"/><circle cx="7" cy="6" r="2" fill="#525252"/></svg>
  <div>Location:<br>Some address goes here</div>
</div>

<div class="abs footer-head" style="left:852px;top:3515px">NEWSLETTER</div>
<p class="abs news-text">Subscribe to our email address to get the latest news.</p>
<div class="abs news-input">
  <svg width="12" height="9" viewBox="0 0 12 9" aria-hidden="true"><rect width="12" height="9" rx="1" fill="#bbb"/></svg>Enter Your Email...
</div>
<div class="abs news-btn"><svg width="16" height="16" viewBox="0 0 16 16" aria-hidden="true"><path d="M1 7l14-6-5 14-2-6z" fill="#fff"/></svg></div>

<div class="abs to-top"><svg width="12" height="14" viewBox="0 0 12 14" aria-hidden="true"><path d="M6 13V2M2 6l4-4 4 4" stroke="#444" stroke-width="1.5" fill="none"/></svg></div>
<div class="abs footer-bar">©2021 BY BRIARLOOM ALL RIGHTS RESERVED</div>

</body>
</html>
```